Vantrel Business Card

I have a business that is called "Vantrel Electrical Products LTD" My company deals with top of the range laptops and mobile phones that are exclusive. I need a business card that will be eye catching but not over complicated.

Target Market(s)

Adults aged 19 to 50
Upper middle class

Industry/Entity Type

Business

Requirements
Must have
• Company name/logo (file attached)
• It must have my contact information which is:

• Name: Dale Marwick

• Position: Managing Director 

• Business Address: 7 Hapton Row, London, W4 9QD

• Contact Number: 02085193604
• Mobile: 07814260537
• Email: info@vantrel-goods.co.uk
Nice to have
• Simple and stylish
• Eye catching

```html
<!DOCTYPE html>
<html lang="en">
<head>
<meta charset="utf-8">
<title>Vantrel Electrical Products – Business Card Options</title>
<link rel="stylesheet" href="https://fonts.googleapis.com/css2?family=Poppins:ital,wght@0,600;1,400&family=Questrial&display=swap">
<style>
  :root {
    --sheet: #dcdcdc;
    --card: #ffffff;
    --band: #02a8d9;
    --brand: #1694c4;
    --ink-deep: #0d6a8c;
    --ink-muted: #2c5566;
    --ink-dark: #111111;
    --rule: #1a6e92;
    --on-band: #ffffff;
  }
  html, body {
    margin: 0;
    width: 1200px;
    height: 1169px;
    overflow: hidden;
    background: var(--sheet);
  }
  .sheet { position: relative; width: 1200px; height: 1169px; }
  .card {
    position: absolute;
    width: 532px;
    height: 344px;
    background: var(--card);
    box-shadow: 3px 3px 4px rgba(0,0,0,0.55);
  }
  .card svg { display: block; width: 532px; height: 344px; }
  .col-left { left: 35px; }
  .col-right { left: 633px; }
  .row-1 { top: 34px; }
  .row-2 { top: 412px; }
  .row-3 { top: 790px; }

  .wordmark { font-family: "Questrial", sans-serif; font-size: 52px; fill: var(--brand); letter-spacing: 2px; }
  .tagline { font-family: "Questrial", sans-serif; font-size: 21.5px; fill: var(--ink-muted); }
  .band { fill: var(--band); }
  .rule { stroke: var(--rule); stroke-width: 1.6; }

  .name-light { font-family: "Questrial", sans-serif; font-size: 23px; }
  .role-light { font-family: "Questrial", sans-serif; font-size: 14px; }
  .name-bold { font-family: "Poppins", sans-serif; font-weight: 600; font-size: 22px; }
  .role-italic { font-family: "Poppins", sans-serif; font-style: italic; font-size: 13.5px; }
  .contact { font-family: "Questrial", sans-serif; font-size: 14px; }

  .on-band { fill: var(--on-band); }
  .on-white { fill: var(--ink-deep); }
  .on-white-dark { fill: var(--ink-dark); }
</style>
</head>
<body>
<main class="sheet">

  <section class="card col-left row-1" aria-label="Card option one">
    <svg viewBox="0 0 532 344">
      <text class="wordmark" x="22" y="76">Vantrel</text>
      <text class="tagline" x="25" y="99">Electrical Products</text>
      <rect class="band" x="0" y="111" width="532" height="233"/>
      <text class="name-light on-band" x="22" y="166">Dale Marwick</text>
      <text class="role-light on-band" x="22" y="182">Managing Director</text>
      <text class="contact on-band" x="24" y="249">7 Hapton Row, London, W4 9QD</text>
      <text class="contact on-band" x="24" y="276">T: 02085193604</text>
      <text class="contact on-band" x="24" y="292">M: 07814 260537</text>
      <text class="contact on-band" x="24" y="308">E: info@vantrel-goods.co.uk</text>
    </svg>
  </section>

  <section class="card col-right row-1" aria-label="Card option two">
    <svg viewBox="0 0 532 344">
      <text class="wordmark" x="22" y="76">Vantrel</text>
      <text class="tagline" x="25" y="99">Electrical Products</text>
      <line class="rule" x1="25" y1="115" x2="201" y2="115"/>
      <text class="contact on-white" x="27" y="250">7 Hapton Row,</text>
      <text class="contact on-white" x="27" y="266">London, W4 9QD</text>
      <text class="contact on-white" x="27" y="282">T: 02085193604</text>
      <text class="contact on-white" x="27" y="298">M: 07814 260537</text>
      <text class="contact on-white" x="27" y="314">info@vantrel-goods.co.uk</text>
      <text class="name-bold on-white" x="433" y="289" text-anchor="middle">Dale Marwick</text>
      <text class="role-italic on-white" x="433" y="305" text-anchor="middle">Managing Director</text>
    </svg>
  </section>

  <section class="card col-left row-2" aria-label="Card option three">
    <svg viewBox="0 0 532 344">
      <text class="wordmark" x="22" y="76">Vantrel</text>
      <text class="tagline" x="25" y="99">Electrical Products</text>
      <text class="contact on-white" x="510" y="50" text-anchor="end">7 Hapton Row,</text>
      <text class="contact on-white" x="507" y="66" text-anchor="end">London, W4 9QD</text>
      <text class="contact on-white" x="510" y="82" text-anchor="end">T: 02085193604 M: 07814 260537</text>
      <text class="contact on-white" x="510" y="98" text-anchor="end">info@vantrel-goods.co.uk</text>
      <rect class="band" x="0" y="111" width="532" height="233"/>
      <text class="name-bold on-band" x="261" y="213" text-anchor="middle">Dale Marwick</text>
      <text class="role-italic on-band" x="261" y="229" text-anchor="middle">Managing Director</text>
    </svg>
  </section>

  <section class="card col-right row-2" aria-label="Card option four">
    <svg viewBox="0 0 532 344">
      <text class="wordmark" x="22" y="76">Vantrel</text>
      <text class="tagline" x="25" y="99">Electrical Products</text>
      <text class="contact on-white" x="507" y="50" text-anchor="end">7 Hapton Row,</text>
      <text class="contact on-white" x="504" y="66" text-anchor="end">London, W4 9QD</text>
      <text class="contact on-white" x="507" y="82" text-anchor="end">T: 02085193604 M: 07814 260537</text>
      <text class="contact on-white" x="507" y="98" text-anchor="end">info@vantrel-goods.co.uk</text>
      <line class="rule" x1="26" y1="115" x2="507" y2="115"/>
      <text class="name-bold on-white" x="260" y="213" text-anchor="middle">Dale Marwick</text>
      <text class="role-italic on-white" x="260" y="229" text-anchor="middle">Managing Director</text>
    </svg>
  </section>

  <section class="card col-left row-3" aria-label="Card option five">
    <svg viewBox="0 0 532 344">
      <text class="wordmark" x="22" y="76">Vantrel</text>
      <text class="tagline" x="25" y="99">Electrical Products</text>
      <rect class="band" x="0" y="111" width="532" height="233"/>
      <text class="name-bold on-band" x="260" y="201" text-anchor="middle">Dale Marwick</text>
      <text class="role-light on-band" x="260" y="218" text-anchor="middle">Managing Director</text>
      <text class="contact on-band" x="264" y="287" text-anchor="middle">7 Hapton Row, London, W4 9QD</text>
      <text class="contact on-band" x="264" y="305" text-anchor="middle">T: 02085193604 M: 07814 260537</text>
      <text class="contact on-band" x="264" y="321" text-anchor="middle">E: info@vantrel-goods.co.uk</text>
    </svg>
  </section>

  <section class="card col-right row-3" aria-label="Card option six">
    <svg viewBox="0 0 532 344">
      <text class="wordmark" x="22" y="76">Vantrel</text>
      <text class="tagline" x="25" y="99">Electrical Products</text>
      <text class="name-light on-white-dark" x="22" y="166">Dale Marwick</text>
      <text class="role-light on-white-dark" x="22" y="182">Managing Director</text>
      <text class="contact on-white-dark" x="24" y="250">7 Hapton Row, London, W4 9QD</text>
      <text class="contact on-white-dark" x="24" y="277">T: 02085193604</text>
      <text class="contact on-white-dark" x="24" y="293">M: 07814 260537</text>
      <text class="contact on-white-dark" x="24" y="309">E: info@vantrel-goods.co.uk</text>
    </svg>
  </section>

</main>
</body>
</html>
```